Wedding Day Custom Wine Label - Tasmanian (Tamar Valley) wine

I am looking for a custom design that will be put on a wine label to commemorate a very good friend's wedding day.

We will need to be able to take the design and print it on to sticker labels that we can put on to wine bottles.

The bride and groom have asked for a simplistic label design (see example image attached). We need two labels. One for "Pinot Noir" wine and the other for "Chardonnay" wine. We would like the label to say:

The Hartwell's
Pinot Noir
2023
Tamar Valley

and for for the other wine variety:

The Hartwell's
Chardonnay
2023
Tamar Valley

smaller text below to say:

13.5% ALC/VOL 750ML
MEGAN & LIAM - 31.10.2024

I am happy to consider other variations - the bride & groom would prefer something minimalistic. Elegant and classy.

Target Market(s)

the bride & groom

Requirements
Must have
• Wedding date (31.10.2024). Wine type (Pinot Noir or Chardonnay).
Should not have
• images not essential

```html
<!DOCTYPE html>
<html lang="en">
<head>
<meta charset="utf-8">
<title>The Hartwell's – Wedding Wine Labels</title>
<link href="https://fonts.googleapis.com/css2?family=Oswald:wght@600&family=Italiana&family=Pinyon+Script&family=Montserrat:wght@400;500&display=swap" rel="stylesheet">
<style>
  :root {
    --backdrop: #fbdcd0;
    --label-top: #ffffff;
    --label-bottom: #ececec;
    --ink: #111111;
    --label-shadow: rgba(120, 70, 50, 0.18);
  }
  * { margin: 0; padding: 0; box-sizing: border-box; }
  html, body {
    width: 1200px;
    height: 1200px;
    overflow: hidden;
    background: var(--backdrop);
  }
  .label-sheet {
    position: relative;
    width: 1200px;
    height: 1200px;
  }
  .wine-label {
    position: absolute;
    top: 280px;
    width: 460px;
    height: 640px;
    background: linear-gradient(180deg, var(--label-top) 0%, var(--label-top) 45%, var(--label-bottom) 100%);
    box-shadow: 0 10px 30px var(--label-shadow);
    color: var(--ink);
    text-align: center;
  }
  .wine-label--pinot { left: 100px; }
  .wine-label--chardonnay { left: 640px; }
  .wine-label > * {
    position: absolute;
    left: 0;
    right: 0;
  }
  .family-name {
    top: 60px;
    font-family: "Oswald", "Arial Narrow", sans-serif;
    font-weight: 600;
    font-size: 54px;
    line-height: 1;
    letter-spacing: -0.5px;
    transform: scaleX(0.82);
  }
  .variety {
    top: 230px;
    line-height: 1;
  }
  .variety--pinot {
    font-family: "Italiana", serif;
    font-size: 86px;
    letter-spacing: -1px;
  }
  .variety--chardonnay {
    top: 236px;
    font-family: "Pinyon Script", cursive;
    font-size: 80px;
    font-weight: 400;
  }
  .vintage {
    top: 356px;
    font-family: "Montserrat", sans-serif;
    font-size: 30px;
    line-height: 1;
  }
  .region {
    top: 394px;
    font-family: "Montserrat", sans-serif;
    font-size: 32px;
    line-height: 1;
  }
  .fine-print {
    top: 572px;
    font-family: "Montserrat", sans-serif;
    font-weight: 500;
    font-size: 14px;
    line-height: 1.7;
    letter-spacing: 0.2px;
  }
</style>
</head>
<body>
  <main class="label-sheet">
    <section class="wine-label wine-label--pinot">
      <h1 class="family-name">The Hartwell's</h1>
      <h2 class="variety variety--pinot">Pinot Noir</h2>
      <p class="vintage">2023</p>
      <p class="region">Tamar Valley</p>
      <p class="fine-print">13.5% ALC/VOL 750ML<br>MEGAN &amp; LIAM - 31.10.2024</p>
    </section>
    <section class="wine-label wine-label--chardonnay">
      <h1 class="family-name">The Hartwell's</h1>
      <h2 class="variety variety--chardonnay">Chardonnay</h2>
      <p class="vintage">2023</p>
      <p class="region">Tamar Valley</p>
      <p class="fine-print">13.5% ALC/VOL 750ML<br>MEGAN &amp; LIAM - 31.10.2024</p>
    </section>
  </main>
</body>
</html>
```